Local Contractor needs Upscale Web Design

This website needs to have an upscale look with a very modern feel.

This is for a home page psd layout

Please build your psd file to match the look of this template: http://www.layoutquarry.example/demo/38162.html

Please change the color scheme to the colors of the attached logo

Add Logo that is attached.

Phone Number:
507-392-4186

Must Include these pages in a horizontal menu bar in this order:
Home, About, Services, Portfolio, Testimonials, Contact

For the rotating banners:
1. Construction - 35+ Years and Growing
2. Capabilities - Complete Line of Services
3. Commitment - Quality and Attention to Detail

Images under rotating banner:
Image 1, 2, 3 (Attached - Crop to fit)

What We're Thinking Section - Change title text to "Retail Space Construction" (Fill the remainder with latin text)

Who Are We Section - Change title text to "Industrial Construction" (Fill the remainder with latin text)

Project Gallery - Image 4, 5, 6, 7 (Attached - Crop to fit)

Remove the sections towards the bottom titled "Why Us" & "Services"

Please make the map show this address:
2917 86th St SW, Pine Hollow, MN 55104

Footer:
Ridgeway Bolt Construction © 2015 | Powered by Marlo Pixel Works

```html
<!DOCTYPE html>
<html lang="en">
<head>
<meta charset="utf-8">
<title>Ridgeway Bolt Construction</title>
<link rel="stylesheet" href="https://fonts.googleapis.com/css2?family=Russo+One&family=Oswald:wght@500;700&family=Roboto:ital,wght@0,400;0,700;1,400&display=swap">
<style>
:root{
  --red:#9b1c22;
  --red-dark:#7c1418;
  --red-bright:#e11b22;
  --red-overlay:#a3232a;
  --ink:#1c1c1c;
  --text:#3a3a3a;
  --white:#ffffff;
  --map:#e8e5df;
  --photo-warm:#6b4f3a;
  --photo-grey:#a9a6a2;
}
*{margin:0;padding:0;box-sizing:border-box}
html,body{width:1200px;height:3112px;overflow:hidden;background:var(--white)}
body{position:relative;font-family:'Roboto',sans-serif;color:var(--text)}
.abs{position:absolute}

/* Hero */
.hero{left:0;top:0;width:1200px;height:615px;background:linear-gradient(180deg,#8e1c22 0%,#b1343a 45%,#8a1a20 100%)}
.logo-panel{left:0;top:0}
.brand{left:48px;top:78px;display:flex;align-items:center;gap:16px;font-family:'Russo One',sans-serif;color:var(--red);font-size:30px;line-height:1.1;text-transform:uppercase}
.brand-mark{width:34px;height:34px;background:var(--red)}
.phone{left:985px;top:8px;display:flex;align-items:center;gap:10px;color:var(--white);font-size:19px}
.main-nav{left:546px;top:80px;display:flex;gap:30px;font-family:'Oswald',sans-serif;font-weight:700;font-size:19px;color:var(--white);text-transform:uppercase}
.main-nav .active{position:relative}
.main-nav .active::after{content:"";position:absolute;left:0;right:0;top:50px;height:4px;background:var(--white)}
.dropdown{left:698px;top:145px;width:184px;padding:10px 14px;background:var(--white);font-family:'Oswald',sans-serif;font-weight:700;font-size:15px;line-height:1.5;color:var(--ink);text-transform:uppercase;box-shadow:0 3px 8px rgba(0,0,0,.3)}
.hero-title{left:48px;top:270px;font-family:'Russo One',sans-serif;font-size:118px;line-height:1;color:var(--white);text-transform:uppercase;white-space:nowrap}
.hero-sub{left:48px;top:398px;font-family:'Roboto',sans-serif;font-weight:700;font-size:58px;color:var(--white);white-space:nowrap}
.dots{left:57px;top:534px;display:flex;gap:24px}
.dots span{width:26px;height:26px;border-radius:50%;background:var(--white)}

/* Feature images */
.photo{background:linear-gradient(160deg,var(--photo-warm),#3d2c22)}
.feat-main{left:59px;top:633px;width:719px;height:460px}
.feat-top{left:806px;top:633px;width:332px;height:214px;background:linear-gradient(180deg,#c9cdd2,#8d6b55)}
.feat-bottom{left:806px;top:871px;width:332px;height:222px;background:linear-gradient(180deg,#b9444a,#8e1c22)}
.feat-label{left:806px;top:1040px;width:332px;text-align:center;font-size:26px;color:var(--white)}

/* Columns */
.col{width:510px}
.col-left{left:59px;top:1160px}
.col-right{left:629px;top:1160px}
.col h2{font-family:'Russo One',sans-serif;font-size:33px;color:var(--red);text-transform:uppercase;line-height:1.15;white-space:nowrap}
.col h3{margin-top:16px;font-family:'Roboto',sans-serif;font-weight:700;font-size:24px;line-height:1.2;color:var(--ink)}
.col p{margin-top:14px;font-size:14.5px;line-height:1.45;color:var(--text)}
.btn{display:inline-block;margin-top:28px;width:235px;height:72px;line-height:72px;text-align:center;background:var(--red);color:var(--white);font-family:'Russo One',sans-serif;font-size:20px;text-transform:uppercase}

/* Section headings */
.section-title{left:59px;font-family:'Russo One',sans-serif;font-size:36px;color:var(--red);text-transform:uppercase;white-space:nowrap}
.rule{left:59px;width:1079px;height:5px;background:var(--red)}
.arrows{left:913px;top:1580px;display:flex}
.arrow{width:76px;height:66px;display:flex;align-items:center;justify-content:center}
.arrow-prev{background:var(--red-overlay)}
.arrow-next{background:#7a3a3d}

/* Gallery */
.tile{width:512px;height:311px}
.g1{left:59px;top:1681px;background:linear-gradient(160deg,#d9d6d1,#5e5750)}
.g2{left:616px;top:1681px;width:522px;background:var(--red)}
.g2-inner{left:719px;top:1740px;width:315px;height:186px;background:linear-gradient(180deg,#9c9891,#d8d4ce)}
.g3{left:59px;top:2040px;background:linear-gradient(160deg,#6a4a33,#2f211a)}
.g4{left:616px;top:2040px;width:522px;background:linear-gradient(160deg,#b8a48c,#3a3430)}

/* Map */
.map{left:0;top:2497px;width:1200px;height:435px;background:var(--map)}
.map-pin{left:420px;top:2590px}
.map-label{left:448px;top:2604px;font-size:13px;color:#555}
.map-rule{left:0;top:2956px;width:1200px;height:3px;background:var(--red)}

/* Footer */
.footer{left:0;top:2988px;width:1200px;height:124px;background:var(--red)}
.footer-text{left:211px;top:3033px;font-style:italic;font-size:22px;color:var(--white);white-space:nowrap}
.to-top{left:940px;top:2988px;width:212px;height:124px;background:var(--red-bright);display:flex;align-items:center;justify-content:center}
</style>
</head>
<body>

<section class="abs hero" role="img" aria-label="Storefront photograph under a red overlay"></section>

<svg class="abs logo-panel" width="540" height="230" viewBox="0 0 540 230" aria-hidden="true">
  <polygon points="0,0 520,0 440,225 0,225" fill="#ffffff" fill-opacity="0.92"/>
</svg>
<div class="abs brand"><span class="brand-mark"></span><span>Ridgeway Bolt<br>Construction</span></div>

<div class="abs phone">
  <svg width="14" height="22" viewBox="0 0 14 22" aria-hidden="true"><rect x="1" y="1" width="12" height="20" rx="2" fill="none" stroke="#fff" stroke-width="2"/><circle cx="7" cy="17" r="1.5" fill="#fff"/></svg>
  <span>507-392-4186</span>
</div>

<nav class="abs main-nav">
  <span class="active">Home</span><span>About</span><span>Services</span><span>Portfolio</span><span>Testimonials</span><span>Contact</span>
</nav>
<div class="abs dropdown">Services Offered-1<br>Services Offered-2</div>

<h1 class="abs hero-title">Commitment</h1>
<p class="abs hero-sub">Quality and Attention to Detail</p>
<div class="abs dots"><span></span><span></span><span></span></div>

<div class="abs photo feat-main" role="img" aria-label="Restaurant building exterior with wooden porch"></div>
<div class="abs feat-top" role="img" aria-label="Retail store building exterior"></div>
<div class="abs feat-bottom" role="img" aria-label="Retail store front under a red overlay"></div>
<div class="abs feat-label">Lorem Ipsum</div>

<article class="abs col col-left">
  <h2>Retail Space Construction</h2>
  <h3>Mauris fermeum dictum magna loreet aliquadr dapibus eget</h3>
  <p>Mauris fermentum dictum magna. Sed laoreet aliquam leo. Ut tellus dolor, dapibus eget, elementum vel, cursus eleifend, elit. Aenean auctor wisi et urna. Aliquam erat volutpat. Duis ac turpis. Integer rutrum ante eu lacus. Vestibulum libero nisl, porta vel, scelerisque eget, malesuada at, neque.</p>
  <span class="btn">Read More</span>
</article>

<article class="abs col col-right">
  <h2>Industrial Construction</h2>
  <h3>Aenean aucto. wisi et urna. Aliqat volutpat. Duisac turpis</h3>
  <p>Nam elit agna, endrerit sit amet, tincidunt ac, viverra sed, nulla. Donec porta diam eu massa. Quisque diam lorem, interdum vitae, dapibus ac, scelerisque vitae, pede. Donec eget tellus non erat lacinia fermentum. Donec in velit vel ipsum auctor pulvinar. Proin ullamcorper urna et felis.</p>
  <span class="btn">Read More</span>
</article>

<h2 class="abs section-title" style="top:1584px">Project Gallery</h2>
<div class="abs arrows">
  <span class="arrow arrow-prev"><svg width="24" height="36" viewBox="0 0 24 36" aria-hidden="true"><polyline points="18,4 6,18 18,32" fill="none" stroke="#fff" stroke-width="6"/></svg></span>
  <span class="arrow arrow-next"><svg width="24" height="36" viewBox="0 0 24 36" aria-hidden="true"><polyline points="6,4 18,18 6,32" fill="none" stroke="#fff" stroke-width="6"/></svg></span>
</div>
<div class="abs rule" style="top:1658px"></div>

<div class="abs tile g1" role="img" aria-label="White kitchen with dark countertops"></div>
<div class="abs tile g2"></div>
<div class="abs g2-inner" role="img" aria-label="Bathroom with freestanding tub"></div>
<div class="abs tile g3" role="img" aria-label="Dark wood kitchen cabinets with farmhouse sink"></div>
<div class="abs tile g4" role="img" aria-label="Stone fireplace wall in living room"></div>

<h2 class="abs section-title" style="top:2396px">Location</h2>
<div class="abs rule" style="top:2467px"></div>

<div class="abs map" role="img" aria-label="Street map showing 2917 86th St SW, Pine Hollow, MN 55104"></div>
<svg class="abs map-pin" width="24" height="34" viewBox="0 0 24 34" aria-hidden="true"><path d="M12 0C5 0 0 5 0 12c0 9 12 22 12 22s12-13 12-22C24 5 19 0 12 0z" fill="#d7262c"/><circle cx="12" cy="12" r="4.5" fill="#fff"/></svg>
<div class="abs map-label">2917 86th St SW</div>
<div class="abs map-rule"></div>

<footer class="abs footer"></footer>
<p class="abs footer-text">Ridgeway Bolt Construction© 2015 | Powered by Marlo Pixel Works</p>
<div class="abs to-top"><svg width="110" height="50" viewBox="0 0 110 50" aria-hidden="true"><polyline points="8,44 55,10 102,44" fill="none" stroke="#fff" stroke-width="12"/></svg></div>

</body>
</html>
```